Re-brand our business and design!

We need a simple informational website (editable for in the future use)
We need our logo(we have included logo), name, who we are, and what we do displayed.

This is our current site (which is not acceptable, and only a template site): all our information is on this site, please use it forreferanceofinformation.
Www.brightlanefixers.com

Target Market(s)

Real estate brokers, and realtors,homeowners, and anyone looking for home repairs.

Industry/Entity Type

Business

Number of Pages Required

4 page

Font styles to use
Sans Serif

Requirements
Must have
• Our name, contact info, services, and our logo (which we will Email upon request)
• MUST have originality to the site.
• custom "contact us form" or request an estimate form.
Nice to have
• page for real customer testimonies.
• page for our previous work where we can upload pics of completed jobs.
Should not have
• any infringements on any copyrights or plagiarism at all.

```html
<!DOCTYPE html>
<html lang="en">
<head>
<meta charset="utf-8">
<title>Brightlane Fixers</title>
<link href="https://fonts.googleapis.com/css2?family=Open+Sans:ital,wght@0,400;0,600;0,700;1,700&display=swap" rel="stylesheet">
<style>
  :root {
    --white: #ffffff;
    --ink: #1c1c1c;
    --text: #444444;
    --muted: #8a8a8a;
    --nav: #7b7b7b;
    --page: #e8e8e8;
    --red: #d80c0c;
    --fb: #3b5998;
    --tw: #1da1f2;
  }
  * { box-sizing: border-box; margin: 0; padding: 0; }
  html, body { width: 1200px; height: 749px; overflow: hidden; }
  body { font-family: "Open Sans", Arial, sans-serif; background: var(--page); position: relative; }

  .site-header { position: absolute; top: 0; left: 0; width: 1200px; height: 119px; background: var(--white); }
  .brand { position: absolute; left: 93px; top: 62px; display: flex; align-items: center; gap: 8px; }
  .brand-mark { width: 14px; height: 14px; background: var(--red); }
  .brand-name { font-size: 17px; font-weight: 700; color: var(--ink); }

  .contact-item { position: absolute; top: 43px; display: flex; align-items: center; gap: 16px; }
  .contact-item.phone { left: 459px; }
  .contact-item.email { left: 655px; }
  .contact-icon { width: 38px; height: 38px; border: 1px solid #9a9a9a; border-radius: 50%; display: flex; align-items: center; justify-content: center; }
  .contact-label { font-size: 10px; letter-spacing: 0.5px; color: var(--muted); text-transform: uppercase; line-height: 14px; }
  .contact-value { font-size: 17px; font-weight: 600; color: var(--muted); line-height: 22px; }

  .social { position: absolute; top: 59px; left: 1059px; display: flex; gap: 9px; }
  .social-square { width: 19px; height: 19px; border: 1px solid var(--fb); }
  .social-square.alt { border-color: var(--tw); background: var(--tw); }

  .main-nav { position: absolute; top: 119px; left: 0; width: 1200px; height: 40px; background: var(--nav); display: flex; justify-content: center; gap: 44px; padding-left: 12px; }
  .main-nav a { color: var(--white); font-size: 14px; font-weight: 600; text-decoration: none; line-height: 40px; letter-spacing: 0.3px; }

  .hero-strip { position: absolute; top: 159px; left: 0; width: 1200px; height: 57px;
    background: linear-gradient(90deg, #4a3a2c 0%, #4f6e2c 18%, #5a8a32 45%, #527a2e 70%, #3f4e24 100%); }

  .intro { position: absolute; top: 270px; left: 0; width: 1200px; text-align: center; }
  .tagline { font-size: 21px; font-weight: 700; font-style: italic; color: #3a3a3a; line-height: 33px; }
  .lead { margin: 14px auto 0; width: 1000px; font-size: 16px; color: var(--text); line-height: 28px; }

  .services { position: absolute; top: 460px; left: 258px; display: flex; gap: 47px; }
  .service-card { width: 196px; height: 256px; background: var(--white); box-shadow: 0 2px 3px rgba(0,0,0,0.18); display: flex; flex-direction: column; align-items: center; }
  .service-card svg { margin-top: 62px; }
  .service-card h3 { margin-top: 28px; font-size: 16px; font-weight: 700; color: #333; text-align: center; line-height: 20px; letter-spacing: 0.3px; }
  .service-card.featured { background: var(--red); box-shadow: 0 6px 22px rgba(216,12,12,0.4); }
  .service-card.featured h3 { color: var(--white); margin-top: 24px; }
</style>
</head>
<body>
  <header class="site-header">
    <div class="brand">
      <span class="brand-mark"></span>
      <span class="brand-name">Brightlane Fixers</span>
    </div>
    <div class="contact-item phone">
      <span class="contact-icon">
        <svg width="18" height="18" viewBox="0 0 24 24" fill="none" stroke="#666" stroke-width="1.6" stroke-linejoin="round"><path d="M6 3l3 4-2 2c1 3 4 6 7 7l2-2 4 3-2 3C10 20 4 14 3 5z"/></svg>
      </span>
      <div>
        <div class="contact-label">Call us</div>
        <div class="contact-value">555-014-2290</div>
      </div>
    </div>
    <div class="contact-item email">
      <span class="contact-icon">
        <svg width="18" height="18" viewBox="0 0 24 24" fill="none" stroke="#666" stroke-width="1.6"><rect x="3" y="6" width="18" height="13"/><path d="M3 6l9 7 9-7"/></svg>
      </span>
      <div>
        <div class="contact-label">Any inquiry email us</div>
        <div class="contact-value">dana@brightlanefixers.com</div>
      </div>
    </div>
    <div class="social">
      <span class="social-square" aria-label="Social link"></span>
      <span class="social-square alt" aria-label="Social link"></span>
    </div>
  </header>

  <nav class="main-nav">
    <a href="#">HOME</a>
    <a href="#">ABOUT US</a>
    <a href="#">TESTIMONIALS</a>
    <a href="#">CONTACT US</a>
  </nav>

  <div class="hero-strip" role="img" aria-label="Garden lawn with stepping stones and flower beds"></div>

  <section class="intro">
    <p class="tagline">One Name, One number, One call means one service for fast timely quotes,<br>home repairs and updates for you and/or your clients.</p>
    <p class="lead">Looking for someone to help get your listing ready to show? A complete Home Repair Solution? Did an inspection reveal repairs needed before closing? Brightlane Fixers can help!</p>
  </section>

  <section class="services">
    <article class="service-card">
      <svg width="84" height="76" viewBox="0 0 84 76" fill="none" stroke="var(--red)" stroke-width="2.4" stroke-linejoin="round">
        <path d="M4 66 L62 14 L72 24 L14 74 Z"/>
        <path d="M62 14 L70 4 L82 16 L72 24"/>
        <rect x="66" y="10" width="6" height="6" transform="rotate(45 69 13)"/>
        <path d="M8 70 l2 3 M14 65 l2 3 M20 60 l2 3 M26 55 l2 3 M32 50 l2 3 M38 45 l2 3 M44 40 l2 3 M50 35 l2 3"/>
      </svg>
      <h3>CARPENTRY</h3>
    </article>
    <article class="service-card featured">
      <svg width="60" height="94" viewBox="0 0 60 94" fill="none" stroke="var(--white)" stroke-width="3" stroke-linejoin="round">
        <path d="M20 2 L28 2 L4 92"/><path d="M28 2 L36 92"/><path d="M20 2 L56 92"/>
        <path d="M22 20 L31 20 M18 38 L36 38 M13 56 L42 56 M9 74 L49 74"/>
      </svg>
      <h3>SMALL<br>CONSTRUCTION</h3>
    </article>
    <article class="service-card">
      <svg width="84" height="84" viewBox="0 0 84 84" fill="none" stroke="var(--red)" stroke-width="2.6" stroke-linejoin="round" stroke-linecap="round">
        <path d="M40 44 C26 50 10 60 6 72 C4 80 12 82 16 76 C22 66 32 56 42 50"/>
        <path d="M44 44 C40 56 30 72 24 80 C20 84 28 86 34 80 C42 70 48 60 52 48"/>
        <path d="M40 44 L60 22 L70 6 L80 12 L72 28 L52 48 Z"/>
        <circle cx="52" cy="40" r="4"/>
      </svg>
      <h3>ELECTRICAL</h3>
    </article>
  </section>
</body>
</html>
```